High profile consulting company needs a Business Card Design

I need a business card design for a coaching /consulting company. We specialize in changing behaviors. Our services include therapy, workshops, life coaching, etc.

Check out our website to get a feel for our personality. www.tidewellpartners.com

The new logo will be attached to the website soon, I have attached the new logo for your use on the business card.
Updates

I forgot to provide you with the company email under the "must have" section for the business card.  The website is:

 www.tidewellpartners.com

I understand there's some trouble with the logo I uploaded.  I will try that again.  Thank you for your efforts.

Dalia

Thank you for some of your questions.  I prefer a one sided business card, and tend to like the white backgrounds.

I also made 2 small changes to the content.  

add MFT after the name:  Dalia Forsythe, MFT

and the tag line needed more clarity once I saw it.  Please change it to:  Helping people and teams grow through clearer talks and lasting new habits.

Thank you,
Dalia

Industry/Entity Type

Business

Requirements
Must have
• logo
Phone number: 321-555-0148
email: Dalia@tidewellpartners.com
Dalia Forsythe, MFT
President
Nice to have
• Helping people and teams grow through clearer talks and lasting new habits.

```html
<!DOCTYPE html>
<html lang="en">
<head>
<meta charset="utf-8">
<title>Tidewell Partners – Business Card Sheet</title>
<link rel="stylesheet" href="https://fonts.googleapis.com/css2?family=Libre+Baskerville:wght@400;700&display=swap">
<style>
  :root {
    --paper: #ffffff;
    --frame: #6c6c71;
    --rule: #e3dfd2;
    --ink: #3a3a3a;
    --ink-soft: #4a4a4a;
    --brand: #4f7a6a;
    --mark: #7a7a7e;
  }
  * { box-sizing: border-box; margin: 0; padding: 0; }
  html, body {
    width: 927px; height: 1200px; overflow: hidden;
    background: var(--paper);
  }
  body { position: relative; font-family: "Libre Baskerville", Georgia, serif; color: var(--ink); }

  .sheet {
    position: absolute; left: 100px; top: 62px;
    display: grid;
    grid-template-columns: 368px 356px;
    grid-auto-rows: 203px;
    column-gap: 18px;
    row-gap: 16px;
  }

  .card {
    border: 6px solid var(--frame);
    background: var(--paper);
    padding: 6px;
  }
  .card__inner {
    height: 100%;
    border: 1.5px solid var(--rule);
    display: grid;
    grid-template-columns: 173px 1fr;
  }

  .card__brand-side {
    border-right: 1.5px solid var(--rule);
    display: grid;
    grid-template-rows: 61px 1fr;
  }
  .brand {
    border-bottom: 1.5px solid var(--rule);
    display: flex; align-items: center; gap: 5px;
    padding: 0 0 8px 10px;
  }
  .brand__dot {
    width: 29px; height: 29px; border-radius: 50%;
    background: var(--mark); flex: none;
  }
  .brand__name {
    font-size: 9.5px; font-weight: 700; line-height: 1.15;
    color: var(--brand); letter-spacing: 0.3px; text-transform: uppercase;
  }
  .tagline {
    align-self: end;
    text-align: center;
    font-size: 9px; line-height: 15px;
    color: var(--ink-soft);
    padding: 0 6px 14px;
  }

  .card__contact-side { padding: 31px 0 0 8px; }
  .person__name { font-size: 13px; font-weight: 700; line-height: 18px; }
  .person__title { font-size: 11.5px; font-weight: 700; line-height: 18px; margin-top: 2px; }
  .contact { margin-top: 20px; font-size: 9px; line-height: 15.5px; color: var(--ink-soft); list-style: none; white-space: nowrap; }
</style>
</head>
<body>
<main class="sheet">
  <!-- card repeated eight times for the print sheet -->
  <article class="card"><div class="card__inner">
    <div class="card__brand-side">
      <div class="brand"><span class="brand__dot"></span><span class="brand__name">Tidewell<br>Partners</span></div>
      <p class="tagline">Helping people and teams grow through clearer talks and lasting new habits.</p>
    </div>
    <div class="card__contact-side">
      <h2 class="person__name">Dalia Forsythe, MFT</h2>
      <p class="person__title">President</p>
      <ul class="contact"><li>T: 321-555-0148</li><li>Dalia@tidewellpartners.com</li><li>www.tidewellpartners.com</li></ul>
    </div>
  </div></article>

  <article class="card"><div class="card__inner">
    <div class="card__brand-side">
      <div class="brand"><span class="brand__dot"></span><span class="brand__name">Tidewell<br>Partners</span></div>
      <p class="tagline">Helping people and teams grow through clearer talks and lasting new habits.</p>
    </div>
    <div class="card__contact-side">
      <h2 class="person__name">Dalia Forsythe, MFT</h2>
      <p class="person__title">President</p>
      <ul class="contact"><li>T: 321-555-0148</li><li>Dalia@tidewellpartners.com</li><li>www.tidewellpartners.com</li></ul>
    </div>
  </div></article>

  <article class="card"><div class="card__inner">
    <div class="card__brand-side">
      <div class="brand"><span class="brand__dot"></span><span class="brand__name">Tidewell<br>Partners</span></div>
      <p class="tagline">Helping people and teams grow through clearer talks and lasting new habits.</p>
    </div>
    <div class="card__contact-side">
      <h2 class="person__name">Dalia Forsythe, MFT</h2>
      <p class="person__title">President</p>
      <ul class="contact"><li>T: 321-555-0148</li><li>Dalia@tidewellpartners.com</li><li>www.tidewellpartners.com</li></ul>
    </div>
  </div></article>

  <article class="card"><div class="card__inner">
    <div class="card__brand-side">
      <div class="brand"><span class="brand__dot"></span><span class="brand__name">Tidewell<br>Partners</span></div>
      <p class="tagline">Helping people and teams grow through clearer talks and lasting new habits.</p>
    </div>
    <div class="card__contact-side">
      <h2 class="person__name">Dalia Forsythe, MFT</h2>
      <p class="person__title">President</p>
      <ul class="contact"><li>T: 321-555-0148</li><li>Dalia@tidewellpartners.com</li><li>www.tidewellpartners.com</li></ul>
    </div>
  </div></article>

  <article class="card"><div class="card__inner">
    <div class="card__brand-side">
      <div class="brand"><span class="brand__dot"></span><span class="brand__name">Tidewell<br>Partners</span></div>
      <p class="tagline">Helping people and teams grow through clearer talks and lasting new habits.</p>
    </div>
    <div class="card__contact-side">
      <h2 class="person__name">Dalia Forsythe, MFT</h2>
      <p class="person__title">President</p>
      <ul class="contact"><li>T: 321-555-0148</li><li>Dalia@tidewellpartners.com</li><li>www.tidewellpartners.com</li></ul>
    </div>
  </div></article>

  <article class="card"><div class="card__inner">
    <div class="card__brand-side">
      <div class="brand"><span class="brand__dot"></span><span class="brand__name">Tidewell<br>Partners</span></div>
      <p class="tagline">Helping people and teams grow through clearer talks and lasting new habits.</p>
    </div>
    <div class="card__contact-side">
      <h2 class="person__name">Dalia Forsythe, MFT</h2>
      <p class="person__title">President</p>
      <ul class="contact"><li>T: 321-555-0148</li><li>Dalia@tidewellpartners.com</li><li>www.tidewellpartners.com</li></ul>
    </div>
  </div></article>

  <article class="card"><div class="card__inner">
    <div class="card__brand-side">
      <div class="brand"><span class="brand__dot"></span><span class="brand__name">Tidewell<br>Partners</span></div>
      <p class="tagline">Helping people and teams grow through clearer talks and lasting new habits.</p>
    </div>
    <div class="card__contact-side">
      <h2 class="person__name">Dalia Forsythe, MFT</h2>
      <p class="person__title">President</p>
      <ul class="contact"><li>T: 321-555-0148</li><li>Dalia@tidewellpartners.com</li><li>www.tidewellpartners.com</li></ul>
    </div>
  </div></article>

  <article class="card"><div class="card__inner">
    <div class="card__brand-side">
      <div class="brand"><span class="brand__dot"></span><span class="brand__name">Tidewell<br>Partners</span></div>
      <p class="tagline">Helping people and teams grow through clearer talks and lasting new habits.</p>
    </div>
    <div class="card__contact-side">
      <h2 class="person__name">Dalia Forsythe, MFT</h2>
      <p class="person__title">President</p>
      <ul class="contact"><li>T: 321-555-0148</li><li>Dalia@tidewellpartners.com</li><li>www.tidewellpartners.com</li></ul>
    </div>
  </div></article>
</main>
</body>
</html>
```